Wine Label Design for a white wine made in the region of San Gimignano, Italy

This is a white wine (crisp and fresh) that is made in the region of San Gimignano, Italy, which is a beautiful hill town in Tuscany famous for it's towers. We would like a classy, elegant front wine label that can also be somewhat fun and whimsical if you prefer. Showcasing or depicting or alluding to the town and the towers of San Gimignano is a plus. The label should state the brand name which is "Vellisora", the varietal, which is Vernaccia di San Gimignano, and the vintage which is 2015. We might change the size of the label slightly but for design purposes please use 5 inches wide x 5 1/2 inches tall. I've uploaded a photo of a successful label design for parameters, but you should not feel limited to this either. Good white wine colors are white and green but we are flexible. Please don't use red, burgundy, or blue colors.

Target Market(s)

This wine label should appeal to all ages but be classy for the older crowd and still eye catching and fun for the millennials. This wine is sold in 15 states in the US, on the East Coast.

Industry/Entity Type

Town

Font styles to use
Serif
Sans Serif

Requirements
Must have
• Referring somehow or depicting the hill town and towers of San Gimignano in some way, such as in silhouette would be a plus. But also try to do something fun and unique with it-- not just an image of the town with words placed over it.
Should not have
• Please don't use the colors blue, reds. Try to think about what makes a wine label classy and sophisticated and 'upmarket' and what makes one cheap and cheesy. We are looking for the classy and sophisticated.

```html
<!DOCTYPE html>
<html lang="en">
<head>
<meta charset="utf-8">
<title>Vellisora – Vernaccia di San Gimignano 2015</title>
<link rel="stylesheet" href="https://fonts.googleapis.com/css2?family=Playfair+Display:wght@400;500&family=Montserrat:wght@400;600&display=swap">
<style>
  :root {
    --backdrop: #e6e6e4;
    --label-paper: #fbfbf8;
    --ink: #1d1d1b;
    --vine-green: #8b9b2e;
    --muted-ink: #555550;
    --photo-light: #cfcfcc;
    --photo-mid: #8e8e8a;
    --photo-dark: #3a3a38;
  }
  * { margin: 0; padding: 0; box-sizing: border-box; }
  html, body {
    width: 781px;
    height: 1200px;
    overflow: hidden;
    background: var(--backdrop);
  }
  .canvas {
    position: relative;
    width: 781px;
    height: 1200px;
  }
  .wine-label {
    position: absolute;
    left: 70px;
    top: 248px;
    width: 640px;
    height: 704px;
    background: var(--label-paper);
    box-shadow: 0 2px 10px rgba(0,0,0,0.08);
    text-align: center;
  }
  .town-photo {
    position: absolute;
    left: 10px;
    top: 10px;
    width: 620px;
    height: 362px;
    background: linear-gradient(180deg, var(--photo-light) 0%, var(--photo-mid) 55%, var(--photo-dark) 100%);
  }
  .brand-name {
    position: absolute;
    left: 0;
    right: 0;
    top: 392px;
    font-family: "Playfair Display", serif;
    font-weight: 400;
    font-size: 92px;
    line-height: 1;
    letter-spacing: 2px;
    color: var(--ink);
    transform: scaleY(1.12);
  }
  .varietal {
    position: absolute;
    left: 0;
    right: 0;
    top: 516px;
    font-family: "Montserrat", sans-serif;
    font-weight: 600;
    font-size: 30px;
    letter-spacing: 3px;
    color: var(--vine-green);
  }
  .appellation {
    position: absolute;
    left: 0;
    right: 0;
    top: 556px;
    font-family: "Montserrat", sans-serif;
    font-weight: 400;
    font-size: 13px;
    letter-spacing: 2px;
    color: var(--muted-ink);
  }
  .vintage {
    position: absolute;
    left: 0;
    right: 0;
    top: 590px;
    font-family: "Playfair Display", serif;
    font-size: 26px;
    letter-spacing: 3px;
    color: var(--ink);
  }
</style>
</head>
<body>
  <main class="canvas">
    <section class="wine-label">
      <div class="town-photo" role="img" aria-label="Black and white photograph of the medieval towers and piazza of San Gimignano"></div>
      <h1 class="brand-name">VELLISORA</h1>
      <p class="varietal">VERNACCIA</p>
      <p class="appellation">DI SAN GIMIGNANO</p>
      <p class="vintage">2015</p>
    </section>
  </main>
</body>
</html>
```